3 glossy INFOGRAPHIC SPLASH PAGES for website of video production / photography studio website

Hello. We need 3 designed infographic images to act as 'splash pages' on our work-in-progress website to offer detailed information to visitors.
1. MUDMAP
2. RATECARD
3. STUDIO FLOORPLAN

To view the website WIP - Go here: http://www.sitevault.com.au/pelbrook/

Regarding FILE SIZES:

The MUDMAP should sit in landscape with dimensions 2048px wide x 1536px high.

The RATECARD and STUDIO FLOORPLAN should be laid out in PORTRAIT with dimensions 1526px wide x 2048px high.

Regarding DESIGNS:

First is a 'MUD MAP' that details travel and parking directions for visitors to our studio,

Second is a floorplan of our studio space, and

Third is a Studio Hire Rate Card.

We want these images to utilise our new theme / branding / logos (attached) and ultimately these designs need to be easily read and understood.

Attached Files (may not be in order in brief, but here is my list):

Target Market(s)

potential studio hire customers (mainly producers)

Industry/Entity Type

Film Production

Font styles to use
Sans Serif
Other font styles liked:
• I have supplied branding fonts to be used as you see fit.

Colors
fbed22
00a990
0292cd
fece3e
f78f20
f37122

Requirements
Must have
• Supplied logos and branding theme / colours (see attached).
• Predominantly gold colour (specific gold supplied) as well as utilising colour theme (see attached)
Nice to have
• Would be nice if all three images have a continuity in their layout / design

```html
<!DOCTYPE html>
<html lang="en">
<head>
<meta charset="utf-8">
<title>Pelbrook Studios – Hire Rates</title>
<link rel="stylesheet" href="https://fonts.googleapis.com/css2?family=Graduate&family=Chakra+Petch:wght@600;700&family=Share+Tech+Mono&display=swap">
<style>
  :root {
    --paper: #f4f3ef;
    --ink: #1e1e1e;
    --gold: #c6a22c;
    --gold-text: #b28f1f;
    --sage: #cfdbc9;
    --grey: #e3e3e1;
    --butter: #f3e49b;
    --cream: #fbf4c8;
    --apricot: #efbc84;
    --rule: #b9a349;
  }
  * { margin: 0; padding: 0; box-sizing: border-box; }
  html, body { width: 894px; height: 1200px; overflow: hidden; background: var(--paper); }
  body { position: relative; font-family: "Share Tech Mono", monospace; color: var(--ink); text-transform: uppercase; }
  .abs { position: absolute; }

  .brand-title { left: 0; width: 894px; top: 26px; text-align: center; font-family: "Graduate", serif; font-weight: 400; font-size: 46px; letter-spacing: 2px; color: var(--gold); }
  .title-dash { top: 56px; width: 22px; height: 6px; background: var(--ink); }
  .doc-label { left: 328px; top: 100px; width: 241px; height: 45px; border: 2px solid var(--gold); display: flex; align-items: center; justify-content: center; font-family: "Chakra Petch", sans-serif; font-weight: 600; font-size: 21px; letter-spacing: 3px; color: var(--gold-text); }
  .effective { left: 0; width: 894px; top: 152px; text-align: center; font-size: 13px; letter-spacing: 3px; color: #7b6a2a; }

  .section-head { left: 40px; width: 814px; display: flex; align-items: center; gap: 14px; }
  .section-head::before, .section-head::after { content: ""; flex: 1; height: 2px; background: var(--rule); }
  .section-head h2 { font-family: "Chakra Petch", sans-serif; font-weight: 700; font-size: 25px; letter-spacing: 1px; white-space: nowrap; line-height: 1; }
  .section-note { left: 0; width: 894px; text-align: center; font-size: 11px; letter-spacing: 1.5px; }

  .rate-box { padding: 11px 18px; font-size: 14.5px; line-height: 20px; }
  .rate-box h3 { font-size: 14.5px; font-weight: 400; margin-bottom: 3px; }
  .sage { background: var(--sage); border-radius: 6px; }
  .grey { background: var(--grey); border-radius: 6px; text-align: center; padding-top: 14px; line-height: 22px; }
  .butter { background: var(--butter); border-radius: 6px; }

  .callout svg { position: absolute; left: 0; top: 0; }
  .callout .txt { position: absolute; text-align: center; font-size: 13px; line-height: 17px; }
  .callout h3 { font-size: 13.5px; font-weight: 400; color: var(--ink); margin-bottom: 2px; }
  .callout p { color: var(--gold-text); }

  .footnote { left: 0; width: 894px; top: 419px; text-align: center; font-size: 10.5px; }

  .extras-text { font-size: 13.5px; line-height: 18.5px; }

  .terms-head { left: 300px; top: 777px; font-family: "Chakra Petch", sans-serif; font-weight: 700; font-size: 26px; line-height: 32px; }
  .terms-col { font-size: 12.8px; line-height: 18px; }
  .terms-col h3 { font-size: 13.5px; font-weight: 400; margin-bottom: 2px; }
  .terms-col p { margin-bottom: 12px; }

  .promise { left: 40px; top: 1011px; width: 814px; height: 74px; background: var(--cream); display: flex; align-items: center; }
  .promise p { font-size: 13.5px; line-height: 17px; }
  .promise .left { width: 360px; padding-left: 22px; }
  .promise .mark { width: 100px; text-align: center; font-size: 15px; color: var(--gold-text); }
  .promise .right { width: 354px; font-size: 12px; line-height: 16px; padding-left: 6px; }

  .notice { left: 40px; top: 1088px; width: 814px; height: 42px; background: var(--apricot); text-align: center; font-size: 11.5px; line-height: 16px; padding-top: 5px; color: #6a4a16; }
  .booking { left: 0; width: 894px; top: 1144px; text-align: center; font-family: "Chakra Petch", sans-serif; font-weight: 600; font-size: 21px; letter-spacing: 1px; }
  .booking svg { vertical-align: -3px; margin: 0 6px; }
</style>
</head>
<body>

<div class="abs title-dash" style="left:150px"></div>
<h1 class="abs brand-title">Pelbrook Studios</h1>
<div class="abs title-dash" style="left:722px"></div>
<div class="abs doc-label">Hire Rates</div>
<div class="abs effective">Effective 1st Jan 2016</div>

<!-- Studio hire -->
<div class="abs section-head" style="top:181px"><h2>Soundproof Studio Hire</h2></div>

<div class="abs rate-box sage" style="left:44px;top:226px;width:389px;height:65px">
  <h3>Bump In/Out</h3>
  <div>$150 P/4hrs &nbsp;Available weekdays only</div>
</div>

<div class="abs callout" style="left:451px;top:222px;width:400px;height:72px">
  <svg width="400" height="72" viewBox="0 0 400 72" aria-hidden="true">
    <polygon points="34,2 386,2 398,14 398,58 386,70 34,70 22,58 22,30 2,4 26,14" fill="none" stroke="var(--gold)" stroke-width="2.5"/>
  </svg>
  <div class="txt" style="left:30px;top:12px;width:360px">
    <h3>Video studio hire includes:</h3>
    <p>10 &amp; 15 amp power outlets,<br>Fibre enabled ethernet &amp; wifi, toilet.</p>
  </div>
</div>

<div class="abs rate-box sage" style="left:44px;top:306px;width:389px;height:100px">
  <h3>Mon to Fri</h3>
  <div>$350 P/Half day - up to 5 hours*<br>$550 P/Full day - up to 10 hours<br>$150 P/HR overtime - beyond 10 hours</div>
</div>

<div class="abs rate-box sage" style="left:451px;top:306px;width:399px;height:100px">
  <h3>Saturday</h3>
  <div>$450 P/Half day - up to 5 hours*<br>$650 P/Full day - up to 10 hours<br>$200 P/HR overtime - beyond 10 hours</div>
</div>

<div class="abs footnote">*Any half day rental that exceeds 5 hours automatically becomes a full day hire.</div>

<!-- Client viewing -->
<div class="abs section-head" style="top:450px"><h2>Dedicated Client Viewing Area</h2></div>
<div class="abs section-note" style="top:483px">To be used in conjunction with studio hire only</div>

<div class="abs callout" style="left:42px;top:502px;width:378px;height:106px">
  <svg width="378" height="106" viewBox="0 0 378 106" aria-hidden="true">
    <polygon points="16,14 2,2 40,14 362,14 376,28 376,90 362,104 16,104 2,90 2,28" fill="none" stroke="var(--gold)" stroke-width="2.5"/>
  </svg>
  <div class="txt" style="left:10px;top:20px;width:358px;font-size:12.5px;line-height:16px">
    <h3>Client area includes:</h3>
    <p>Coffee machine, bottled water, fridge,<br>65" 4K viewing monitor, leather couch,<br>boardroom table, additional bathroom<br>&amp; toilet, Fibre enabled ethernet &amp; wifi.</p>
  </div>
</div>

<div class="abs rate-box grey" style="left:461px;top:529px;width:185px;height:71px">Mon to Fri<br>$250 P/Day</div>
<div class="abs rate-box grey" style="left:668px;top:529px;width:186px;height:71px">Saturday<br>$300 P/Day</div>

<!-- Extras -->
<div class="abs section-head" style="top:628px"><h2>Extras</h2></div>

<div class="abs butter" style="left:44px;top:661px;width:392px;height:111px">
  <div class="abs extras-text" style="left:14px;top:9px;width:310px">
    <div>Equipment:</div>
    Reference monitor, C-stands, lighting stands, fabric green-screen etc. are available on request for additional fees.
  </div>
  <svg class="abs" style="left:334px;top:30px" width="44" height="48" viewBox="0 0 44 48" aria-label="Equipment icon" role="img">
    <rect x="4" y="4" width="26" height="38" rx="3" fill="none" stroke="#8a7420" stroke-width="2"/>
    <circle cx="17" cy="15" r="4" fill="none" stroke="#8a7420" stroke-width="2"/>
    <circle cx="17" cy="30" r="7" fill="none" stroke="#8a7420" stroke-width="2"/>
    <line x1="34" y1="26" x2="42" y2="44" stroke="#8a7420" stroke-width="2.5"/>
    <circle cx="33" cy="23" r="4" fill="#8a7420"/>
  </svg>
</div>

<div class="abs butter" style="left:448px;top:661px;width:290px;height:96px">
  <div class="abs extras-text" style="left:14px;top:16px;width:200px">
    <div>Catering:</div>
    Contact us for healthy, fresh, locally sourced catering options.
  </div>
  <svg class="abs" style="left:222px;top:22px" width="34" height="50" viewBox="0 0 34 50" aria-label="Cutlery icon" role="img">
    <path d="M4 2 V16 Q4 22 10 22 Q16 22 16 16 V2 M10 2 V48" fill="none" stroke="#8a7420" stroke-width="2.5"/>
    <path d="M28 48 V2 Q20 10 22 28 H28" fill="none" stroke="#8a7420" stroke-width="2.5"/>
  </svg>
</div>

<div class="abs callout" style="left:727px;top:661px;width:127px;height:108px">
  <svg width="127" height="108" viewBox="0 0 127 108" aria-hidden="true">
    <polygon points="36,2 91,2 125,32 125,76 91,106 36,106 2,76 2,32" fill="var(--paper)" stroke="var(--gold)" stroke-width="2.5"/>
  </svg>
  <div class="txt" style="left:14px;top:20px;width:99px;font-size:11.5px;line-height:16px">
    <p>Gluten free and vegetarian options also available.</p>
  </div>
</div>

<!-- Terms -->
<svg class="abs" style="left:40px;top:786px" width="814" height="196" viewBox="0 0 814 196" aria-hidden="true">
  <path d="M 4 8 L 4 192 L 810 192 L 810 8 L 538 8" fill="none" stroke="var(--rule)" stroke-width="3"/>
  <path d="M 4 8 L 246 8" fill="none" stroke="var(--rule)" stroke-width="3"/>
  <polygon points="244,-2 264,8 244,18" fill="var(--rule)"/>
</svg>
<div class="abs terms-head">Terms &amp; Conditions</div>

<div class="abs terms-col" style="left:62px;top:814px;width:330px">
  <h3>Payment:</h3>
  <p>14 day account terms applies to all verified account holders, otherwise payment must be made in full at end of usage via card or cash.</p>
  <h3>Cancellation:</h3>
  <p>Cancellation fees apply to bookings cancelled less than 24 hours before agreed studio hire start time.</p>
</div>

<div class="abs terms-col" style="left:406px;top:814px;width:428px">
  <h3>Damage policy:</h3>
  <p>Pelbrook Studios understands that sometimes things happen, and general wear and tear is an unavoidable fact of life. However, if significant damage or breakages occur, the cost of repair or replacement will be placed solely onto the hirer. We also expect our studio wall to be left in the same relative condition as it was found, and any significant damage will result in a replastering and repainting fee of $300.</p>
</div>

<!-- Promise band -->
<div class="abs promise">
  <p class="left">At Pelbrook Studios, we endeavour to make your shooting experience run as smoothly as possible.</p>
  <p class="mark">Pelbrook</p>
  <p class="right">We are here to listen to your requirements and assist you in any way, so feel free to contact us well before your shoot to discuss how we can help.</p>
</div>

<div class="abs notice">Pelbrook Studios is equipped with 24 hour CCTV and is fully alarmed.<br>All prices above are exclusive of GST.</div>

<div class="abs booking">For studio bookings
  <svg width="22" height="20" viewBox="0 0 22 20" aria-label="Phone" role="img">
    <path d="M2 7 Q11 0 20 7 L18 10 L14 8 V6 Q11 5 8 6 V8 L4 10 Z" fill="none" stroke="var(--ink)" stroke-width="1.6"/>
    <rect x="5" y="10" width="12" height="8" rx="1.5" fill="none" stroke="var(--ink)" stroke-width="1.6"/>
    <circle cx="11" cy="14" r="2" fill="var(--ink)"/>
  </svg>03 9555 0172</div>

</body>
</html>
```